I need business cards for a company that will be an umbrella for many retail stores. I need them to be sleek and modern. I would like some white and black in the background of the card as these are the office colours the logo is attached.
Target Market(s)
worldwide
Industry/Entity Type
Business
Requirements
Must have
- traditional business card shape
Should not have
- too many colours
no swirly text

```html
<!DOCTYPE html>
<html lang="en">
<head>
<meta charset="utf-8">
<title>Norva General Trading – Business Cards</title>
<link rel="stylesheet" href="https://fonts.googleapis.com/css2?family=Open+Sans:wght@400&display=swap">
<style>
  :root {
    --stage-light: #f7f7f7;
    --stage-dark: #c9cacc;
    --card-grey: #e9eaec;
    --blue-deep: #1b64ad;
    --blue-band: #8fb0da;
    --blue-soft: #dfe7f3;
    --blue-mist: #a9bfe2;
    --ink: #2f3033;
  }
  * { margin: 0; padding: 0; box-sizing: border-box; }
  html, body { width: 1200px; height: 900px; overflow: hidden; }
  body {
    position: relative;
    font-family: "Open Sans", sans-serif;
    color: var(--ink);
    background: radial-gradient(ellipse 70% 70% at 42% 48%, var(--stage-light) 0%, #e4e5e6 60%, var(--stage-dark) 100%);
  }
  .card { position: absolute; width: 709px; height: 433px; overflow: hidden; }
  .card svg { position: absolute; inset: 0; }
  .card--back { left: 369px; top: 429px; background: linear-gradient(180deg, #eceef0 0%, #e3e7ec 30%, var(--blue-mist) 100%); }
  .card--front { left: 124px; top: 40px; }

  .brand { position: absolute; display: flex; align-items: center; gap: 18px; }
  .brand__mark { border-radius: 50%; background: var(--blue-deep); flex: none; }
  .brand__name { font-weight: 400; color: var(--ink); line-height: 1.15; letter-spacing: 0.04em; }
  .brand__name span { display: block; }

  .card--front .brand { left: 40px; top: 68px; }
  .card--front .brand__mark { width: 44px; height: 44px; }
  .card--front .brand__line1 { font-size: 25px; }
  .card--front .brand__line2 { font-size: 18px; }

  .card--back .brand { left: 214px; top: 165px; }
  .card--back .brand__mark { width: 52px; height: 52px; }
  .card--back .brand__line1 { font-size: 28px; }
  .card--back .brand__line2 { font-size: 20px; }

  .contact { position: absolute; left: 50px; top: 216px; }
  .contact__name { font-size: 24px; line-height: 34px; }
  .contact__line { font-size: 19px; line-height: 29.5px; }

  .address { position: absolute; right: 32px; top: 360px; text-align: right; font-size: 18px; line-height: 27px; }
</style>
</head>
<body>

  <section class="card card--back" aria-label="Card back">
    <div class="brand">
      <span class="brand__mark"></span>
      <p class="brand__name"><span class="brand__line1">Norva</span><span class="brand__line2">General Trading</span></p>
    </div>
  </section>

  <section class="card card--front" aria-label="Card front">
    <svg width="709" height="433" viewBox="0 0 709 433" aria-hidden="true">
      <defs>
        <linearGradient id="front-band" x1="0" y1="1" x2="1" y2="0">
          <stop offset="0" stop-color="#93b0da"/>
          <stop offset="0.6" stop-color="#c8d6ec"/>
          <stop offset="1" stop-color="#e3eaf5"/>
        </linearGradient>
        <radialGradient id="header-glow" cx="0.25" cy="0.45" r="0.8">
          <stop offset="0" stop-color="#ffffff"/>
          <stop offset="0.45" stop-color="#e4ebf6"/>
          <stop offset="1" stop-color="#a8bfe1"/>
        </radialGradient>
      </defs>
      <rect width="709" height="433" fill="url(#front-band)"/>
      <ellipse cx="196" cy="128" rx="390" ry="258" fill="var(--blue-band)"/>
      <ellipse cx="186" cy="120" rx="382" ry="250" fill="var(--card-grey)"/>
      <ellipse cx="180" cy="88" rx="194" ry="93" fill="var(--blue-band)"/>
      <ellipse cx="150" cy="82" rx="196" ry="97" fill="url(#header-glow)"/>
    </svg>

    <div class="brand">
      <span class="brand__mark"></span>
      <p class="brand__name"><span class="brand__line1">Norva</span><span class="brand__line2">General Trading</span></p>
    </div>

    <div class="contact">
      <p class="contact__name">Name here</p>
      <p class="contact__line">Job Title</p>
      <p class="contact__line">Phone : +0123456789</p>
      <p class="contact__line">Phone : +0123456789</p>
    </div>

    <address class="address" style="font-style: normal;">
      <p>Harbor Line avenue</p>
      <p>PO BOX 412 VIC</p>
    </address>
  </section>

</body>
</html>
```